依頼詳細
病院で使用する診察券のデザインです。
シンプルで分かりやすいデザインでお願いします。
記載項目
表面:病院名、電話番号
裏面:診療時間、飼い主名、ペット名、注意事項
希望イメージ
シンプル 複雑
単色 カラフル
暗い 明るい
日常 高級
遊び心 厳粛
未来的 伝統的
女性的 男性的
希望する色
緑系
納品ファイル
補足説明
■ 選んだ理由

こちらの要望に合った提案をしていただき、デザインの構成もイメージ通りでした。

■ 提案者全員のお礼・コメント

こんなにたくさんのご提案をいただけるとは思いませんでした。本当にありがとうございました。また利用する際にはよろしくお願いします。

```html
<!DOCTYPE html>
<html lang="ja">
<head>
<meta charset="utf-8">
<title>ふたばの犬猫病院 診察券</title>
<link href="https://fonts.googleapis.com/css2?family=M+PLUS+Rounded+1c:wght@400;500;700;800&display=swap" rel="stylesheet">
<style>
  :root {
    --green: #1f5c34;
    --green-soft: #e4eee6;
    --line: #c9d6cc;
    --card-edge: #cfcfcf;
    --paper: #ffffff;
    --ink: #1f5c34;
  }
  * { box-sizing: border-box; margin: 0; padding: 0; }
  html, body { width: 832px; height: 1200px; overflow: hidden; background: var(--paper); }
  body { font-family: "M PLUS Rounded 1c", sans-serif; color: var(--ink); position: relative; }

  .card {
    position: absolute; left: 4px; width: 824px;
    border: 2px solid var(--card-edge); border-radius: 26px;
    overflow: hidden; background: var(--paper);
  }
  .card--front { top: 4px; height: 516px; }
  .card--back { top: 612px; height: 584px; }

  /* front */
  .ticket-label {
    position: absolute; top: 20px; left: 50%; transform: translateX(-50%);
    width: 250px; height: 56px; border-radius: 28px; background: var(--green);
    color: #fff; font-weight: 800; font-size: 34px; letter-spacing: 14px;
    display: flex; align-items: center; justify-content: center; padding-left: 14px;
  }
  .clinic-name {
    position: absolute; top: 112px; left: 0; right: 0;
    display: flex; justify-content: center; align-items: center; gap: 22px;
  }
  .clinic-name__dot { width: 30px; height: 30px; border-radius: 50%; background: var(--green); flex: none; }
  .clinic-name__text { font-weight: 800; font-size: 62px; line-height: 1.08; }
  .clinic-en {
    position: absolute; top: 296px; left: 0; right: 0; text-align: center;
    font-weight: 700; font-size: 21px; letter-spacing: 3px; line-height: 1;
  }
  .front-band { position: absolute; left: 0; bottom: 0; width: 100%; height: 200px; }
  .phone {
    position: absolute; left: 0; right: 0; bottom: 42px;
    display: flex; justify-content: center; align-items: center; gap: 14px;
    color: #fff; font-weight: 700; font-size: 62px; letter-spacing: 2px; line-height: 1;
  }

  /* back */
  .owner-band {
    position: absolute; top: 0; left: 0; width: 100%; height: 190px;
    background: var(--green); border-radius: 0 0 40px 40px;
  }
  .name-field {
    position: absolute; top: 44px; height: 100px; width: 360px;
    background: #fff; border-radius: 50px;
    display: flex; align-items: center; justify-content: flex-end;
    padding-right: 30px; font-size: 24px; font-weight: 500;
  }
  .name-field--owner { left: 34px; }
  .name-field--pet { left: 412px; }

  .hours {
    position: absolute; top: 226px; left: 40px; width: 740px;
    border-collapse: collapse; font-size: 25px; font-weight: 500; text-align: center;
  }
  .hours th { background: var(--green-soft); font-weight: 700; height: 46px; }
  .hours td { height: 54px; border-bottom: 2px solid var(--line); }
  .hours th:first-child, .hours td:first-child { width: 190px; text-align: left; padding-left: 14px; }
  .closed-note { position: absolute; top: 398px; left: 44px; font-size: 22px; font-weight: 500; }
  .notes { position: absolute; top: 466px; left: 44px; font-size: 19px; line-height: 44px; font-weight: 500; list-style: none; }
  .notes li::before { content: "●"; margin-right: 4px; }
  .back-sign { position: absolute; top: 470px; right: 36px; text-align: left; }
  .back-sign__name { font-weight: 700; font-size: 32px; line-height: 1.2; }
  .back-sign__address { font-size: 19px; margin-top: 6px; }
</style>
</head>
<body>
  <section class="card card--front">
    <div class="ticket-label">診察券</div>
    <div class="clinic-name">
      <span class="clinic-name__dot"></span>
      <p class="clinic-name__text">ふたばの<br>犬猫病院</p>
    </div>
    <p class="clinic-en">FUTABA ANIMAL CLINIC</p>
    <svg class="front-band" viewBox="0 0 824 200" preserveAspectRatio="none" aria-hidden="true">
      <path d="M0 0 Q412 100 824 0 L824 200 L0 200 Z" fill="#1f5c34"/>
    </svg>
    <div class="phone">
      <svg width="48" height="48" viewBox="0 0 24 24" aria-hidden="true">
        <path fill="#fff" d="M6.6 10.8a15.2 15.2 0 0 0 6.6 6.6l2.2-2.2a1 1 0 0 1 1-.25 11.4 11.4 0 0 0 3.6.57 1 1 0 0 1 1 1V20a1 1 0 0 1-1 1A17 17 0 0 1 3 4a1 1 0 0 1 1-1h3.5a1 1 0 0 1 1 1c0 1.25.2 2.45.57 3.6a1 1 0 0 1-.25 1z"/>
      </svg>
      <span>00-987-6543</span>
    </div>
  </section>

  <section class="card card--back">
    <div class="owner-band"></div>
    <div class="name-field name-field--owner">様</div>
    <div class="name-field name-field--pet">ちゃん</div>

    <table class="hours">
      <tr><th>診療時間</th><th>月</th><th>火</th><th>水</th><th>木</th><th>金</th><th>土</th><th>日祝</th></tr>
      <tr><td>0:00〜00:00</td><td>○</td><td>○</td><td>○</td><td>○</td><td>○</td><td>○</td><td>－</td></tr>
      <tr><td>00:00〜00:00</td><td>○</td><td>○</td><td>○</td><td>○</td><td>○</td><td>○</td><td>－</td></tr>
    </table>
    <p class="closed-note">●休診日：○曜・○曜・日曜祝日</p>

    <ul class="notes">
      <li>ご来院の際は診察券を受付にお出しください</li>
      <li>○○○○○○○○○○○○○○○○○</li>
    </ul>
    <div class="back-sign">
      <p class="back-sign__name">ふたばの犬猫病院</p>
      <p class="back-sign__address">緑川県青葉市若葉町12-3</p>
    </div>
  </section>
</body>
</html>
```